Health Coaching Brochure for Healthcare Practioners

I am looking to have a tri-fold brochure created marketed towards healthcare practitioners (doctors, nurses, surgeons, etc), to get them to purchase 1-on-1 health coaching from me.
I've provided the text/content (in pdf & pages), my logo, a picture of me, and two color palettes, but please also include lots of white space. I would like to design to be very clean, modern & crisp. Also include additional photos, of doctors, etc taking care of themselves & feeling happy (maybe eating healthy, maybe exercising, feeling good & happy!)
Please also see http://brightmeadowwellness.com and http://instagram.com/brightmeadowwellness for a feel of my brand.
Thank you!
Target Market(s)
Healthcare Practioners (mainly based in Los Angeles, for now)
Industry/Entity Type
Healthcare
Look and feel

```html
<!DOCTYPE html>
<html lang="en">
<head>
<meta charset="utf-8">
<title>Bright Meadow Wellness – Health Coaching for Healthcare Practitioners</title>
<link rel="stylesheet" href="https://fonts.googleapis.com/css2?family=Open+Sans:wght@400;600;700;800&family=Signika:wght@400;500;600;700&display=swap">
<style>
:root{
  --teal:#17b1c2;
  --red:#8b1e2e;
  --blue:#1c73ad;
  --heading-blue:#1a7cb6;
  --ink:#333;
  --grey-box:#e9ebed;
  --backdrop:#6b4426;
  --white:#fff;
  --sans:"Open Sans",Arial,sans-serif;
  --display:"Signika","Open Sans",sans-serif;
}
*{box-sizing:border-box;margin:0;padding:0}
html,body{width:1200px;height:796px;overflow:hidden;background:var(--backdrop);font-family:var(--sans);color:var(--ink)}
.page{position:absolute;width:546px;height:706px;background:var(--white);overflow:hidden}
.page--front{left:41px;top:42px}
.page--back{left:613px;top:41px;height:707px}
.abs{position:absolute}

/* FRONT */
.front-top{left:0;top:0;width:546px;height:388px;background:var(--teal);color:var(--white)}
.front-title{left:39px;top:28px;font-weight:800;font-size:25px}
.front-sub{left:39px;top:62px;width:380px;font-weight:700;font-size:18px;line-height:25px}
.portrait{left:428px;top:25px;width:88px;height:99px;border:2px solid var(--white);border-radius:8px;background:linear-gradient(160deg,#d9d4cf,#5a3b2e 55%,#efe9e4)}
.features{left:39px;top:144px;width:270px}
.features h3{font-size:10.5px;font-weight:600;line-height:14px;margin-bottom:3px}
.features ul{list-style:none;margin-bottom:6px}
.features li{font-size:8.4px;line-height:13.4px;padding-left:12px;position:relative}
.features li::before{content:"";position:absolute;left:0;top:4px;width:4px;height:4px;border-radius:50%;background:#e0262b}
.features p{font-size:10.5px;font-weight:600;margin-top:7px}
.call-box{left:313px;top:150px;width:204px;height:214px;background:var(--grey-box);border:2px solid var(--white);border-radius:10px;text-align:center;color:#222;box-shadow:0 2px 4px rgba(0,0,0,.25)}
.call-box .lead{margin-top:10px;font-family:var(--display);font-size:16px;font-weight:500;color:var(--red)}
.call-box .phone{font-family:var(--display);font-size:30px;font-weight:700;color:var(--red);line-height:34px}
.call-box .small{font-size:12px;font-weight:700;margin-top:10px}
.call-box .email{font-size:9px;font-weight:600}
.call-box .service{font-size:12.5px;font-weight:600;line-height:18px;margin-top:4px}
.call-box .offer{font-family:var(--display);font-size:20px;font-weight:600;color:var(--blue);line-height:24px;margin-top:10px}
.intro{left:39px;top:400px;width:210px;font-size:8px;line-height:13.2px;text-align:justify;color:#444}
.pledge{left:302px;top:400px;width:230px;font-size:9px;line-height:14px;font-weight:600;color:var(--red)}
.pledge strong{display:block;margin-top:4px;font-family:var(--display);font-size:14.5px;color:var(--teal);font-weight:600}
.food{top:472px;height:134px}
.feel-title{left:33px;top:614px;font-family:var(--display);font-size:18px;font-weight:600;color:var(--red)}
.feel-band{left:0;top:642px}
.feel-list{left:33px;top:648px;font-size:10.3px;line-height:16px;font-weight:600;color:var(--white)}
.map-box{left:307px;top:586px;width:204px;height:104px;background:#f0f1f2;border:2px solid var(--white);border-radius:10px;display:flex;align-items:center;justify-content:center;font-size:26px;color:#666;box-shadow:0 1px 3px rgba(0,0,0,.2)}

/* BACK */
.runner{left:147px;top:0;width:399px;height:391px;background:linear-gradient(90deg,#fff 0%,rgba(255,255,255,.4) 20%,rgba(200,190,180,.6) 45%,#b9a89b 65%,#8e7d72 100%)}
.brand{left:30px;top:54px;font-size:22px;font-weight:700;color:#111}
.back-headline{left:29px;top:115px;font-family:var(--display);font-size:25px;font-weight:600;line-height:34px;color:var(--heading-blue)}
.tab{left:0;top:237px;width:290px;height:56px;background:var(--red);border-radius:0 22px 22px 0;color:var(--white);padding:6px 0 0 29px}
.tab b{display:block;font-family:var(--display);font-size:22px;font-weight:600;line-height:28px}
.tab span{font-size:12.5px}
.trainer{left:29px;top:320px;width:270px;color:var(--red)}
.trainer h2{font-family:var(--display);font-size:23px;font-weight:400;letter-spacing:.3px}
.trainer p{font-size:10.5px;line-height:15px}
.trainer .mail{font-size:12.5px;font-weight:700}
.badge{left:321px;top:297px;width:116px;height:116px;border-radius:50%;background:var(--white);border:5px solid var(--teal);display:flex;align-items:center;justify-content:center;text-align:center;font-family:var(--display);font-size:20px;font-weight:700;line-height:21px;color:#111;z-index:2;box-shadow:0 2px 5px rgba(0,0,0,.3)}
.back-panel{left:0;top:391px;width:546px;height:272px;background:var(--teal);color:var(--white)}
.consult{left:29px;top:26px;width:210px;font-family:var(--display);font-size:22px;font-weight:600;line-height:25px}
.consult .phone{font-size:28px;margin-top:8px;display:block}
.rule{left:29px;top:124px;width:200px;height:2px;background:var(--white)}
.sessions{left:29px;top:143px;width:215px;font-family:var(--display);font-size:16px;line-height:22px}
.sessions b{font-size:21px;font-weight:600;line-height:24px}
.divider{left:253px;top:20px;width:1px;height:240px;background:rgba(255,255,255,.35)}
.about{left:268px;top:16px;width:251px}
.about h3{font-family:var(--display);font-size:16px;font-weight:600;margin-bottom:10px}
.about p{font-size:7.7px;line-height:11.6px;text-align:justify;margin-bottom:10px}
.back-foot{left:0;top:663px}
.foot-contact{left:28px;top:674px;font-family:var(--display);color:var(--white);font-size:13px;font-style:italic;font-weight:600}
.foot-contact b{font-style:normal;font-size:20px}
.foot-web{left:265px;top:674px;font-family:var(--display);font-size:16.5px;font-weight:600;color:var(--white);letter-spacing:.3px}
</style>
</head>
<body>

<section class="page page--front">
  <div class="abs front-top">
    <h1 class="abs front-title">Care for the carers!</h1>
    <p class="abs front-sub">You look after your patients all day – ready to make your own health the priority?</p>
    <div class="abs portrait" role="img" aria-label="Portrait photo of the coach"></div>
    <div class="abs features">
      <h3>Get the most out of a busy schedule by working with a dedicated health coach</h3>
      <ul>
        <li>Customized health plan, built around long shifts</li>
        <li>Provide motivation, support, and accountability</li>
      </ul>
      <h3>Reach your wellness goals and enjoy doing it</h3>
      <ul>
        <li>Stress &amp; Burnout Recovery</li><li>Energy for Long Shifts</li><li>Sleep &amp; Recovery Habits</li>
        <li>Weight Management</li><li>Healthy Meal Planning</li>
        <li>Body Composition Analysis</li><li>Specialized Diet Plans</li>
        <li>Nutrition &amp; Supplementation Counseling</li><li>Movement Between Shifts</li>
      </ul>
      <p>Integrative Nutrition &amp; Health Coaching available</p>
      <p>+24 hour access to coach</p>
    </div>
    <div class="abs call-box">
      <p class="lead">Call to Lena on</p>
      <p class="phone">000-0000-000</p>
      <p class="small">or email</p>
      <p class="email">lena@brightmeadowwellness.com</p>
      <p class="service">One-on-One<br>Health Coaching</p>
      <p class="offer">15 Minute FREE<br>Consultation</p>
    </div>
  </div>

  <p class="abs intro">Helping others is my passion. Doctors, nurses and surgeons care for patients every day, yet rarely find time to care for themselves. Together we build simple habits that give back energy, focus and calm, on and off shift.</p>
  <p class="abs pledge">Working with practitioners of every specialty and schedule, I fit coaching around your shifts, with small steps toward a healthier life.<strong>let's do it together!</strong></p>

  <div class="abs food" style="left:0;width:98px;background:linear-gradient(135deg,#3a2418,#7a5440)" role="img" aria-label="Photo of dark chocolate bites"></div>
  <div class="abs food" style="left:101px;width:115px;background:linear-gradient(135deg,#8a5a2a,#5f8a3a 60%,#e8e6e0)" role="img" aria-label="Photo of a green smoothie bowl"></div>
  <div class="abs food" style="left:221px;width:132px;background:linear-gradient(135deg,#5a7a3a,#c87a3a 50%,#b83040)" role="img" aria-label="Photo of prepared healthy meal containers"></div>
  <div class="abs food" style="left:357px;width:92px;background:linear-gradient(160deg,#f2efea,#8a5a40 60%,#e8e4de)" role="img" aria-label="Photo of a protein shake"></div>
  <div class="abs food" style="left:454px;width:92px;background:linear-gradient(160deg,#f4f4ef,#6aa040 60%,#eef0e8)" role="img" aria-label="Photo of a green juice"></div>

  <h2 class="abs feel-title">How would it feel to</h2>
  <svg class="abs feel-band" width="546" height="64" viewBox="0 0 546 64" aria-hidden="true">
    <polygon points="0,0 280,0 302,22 546,22 546,64 0,64" fill="var(--red)"/>
  </svg>
  <p class="abs feel-list">Finish a long shift with energy to spare?<br>Finally get a handle on food and your cravings?<br>Care for yourself as well as your patients?</p>
  <div class="abs map-box" role="img" aria-label="Map of the studio location">map</div>
</section>

<section class="page page--back">
  <div class="abs runner" role="img" aria-label="Photo of a woman running on a bridge"></div>
  <p class="abs brand">Bright Meadow Wellness</p>
  <h1 class="abs back-headline">Healthy Habits for Those<br>Who Care for Others<br>Feel Better Than Ever</h1>
  <div class="abs tab"><b>1-on-1 Health Coaching</b><span>For Healthcare Practitioners, LA</span></div>
  <div class="abs trainer">
    <h2>LENA MARSH</h2>
    <p>Holistic Health Coach for Healthcare Teams</p>
    <p class="mail">lena@brightmeadowwellness.com</p>
  </div>
  <div class="abs badge">+24<br>hour<br>access to<br>coach</div>

  <div class="abs back-panel">
    <p class="abs consult">Call for a free 15 minute consultation<span class="phone">000 0000 0000</span></p>
    <div class="abs rule"></div>
    <p class="abs sessions"><b>Coaching sessions</b> are held in a Private Studio in Glendale, CA or <b style="font-size:18px">online.</b></p>
    <div class="abs divider"></div>
    <div class="abs about">
      <h3>About me</h3>
      <p>Lena Marsh is a holistic health coach, fitness nutritionist, and personal trainer based in Los Angeles, California. Lena helps doctors, nurses and surgeons improve their health, build sustainable habits, and feel their best.</p>
      <p>Lena sought fitness in 2005 to overcome her lifelong battle of depression, anxiety, and an extra 30 pounds. After completely transforming her body and her mind, she saw that change spill over to other areas of her life – career, relationships, and self-worth. Now she helps busy clinicians transform their lives, as well.</p>
      <p>Fitness was only the beginning. Lena's journey has grown into a holistic approach made for demanding schedules. She puts strong emphasis on energy, sleep and longevity, and believes proper digestion is key to feeling well and preventing disease.</p>
    </div>
  </div>

  <svg class="abs back-foot" width="546" height="44" viewBox="0 0 546 44" aria-hidden="true">
    <rect width="546" height="44" fill="var(--blue)"/>
    <polygon points="0,0 248,0 232,44 0,44" fill="var(--red)"/>
    <polygon points="248,0 262,0 246,44 232,44" fill="var(--teal)"/>
  </svg>
  <p class="abs foot-contact">Contact me : <b>000 0000 000</b></p>
  <p class="abs foot-web">www.brightmeadowwellness.com</p>
</section>

</body>
</html>
```